Meadowtail Pet Business Card

We need a business card designed with two sides to it. I would like the front of the card to be mostly graphic and the back of the card to have the bullet points of our pet food.

I don't have a telephone number for the business yet so just leave a space for a toll free number. (800) xxx-xxxx.

Thanks,

Tobias

Combination Diet
Chicken Diet
Beef Diet
Lamb Diet

Website:  www.meadowtailpet-example.net

email:  rwelby@meadowtailpet-example.net

Direct - 347-xxx-xxxx
Toll Free - xxx-xxx-xxxx

www.meadowtailpet-example.net

Ravi Welby (Example)
Customer Experience Officer

rwelby@meadowtailpet-example.net
Direct - (347) xxx-xxxx

Sales Inquiries - (800) xxx-xxxx

All,

Please include the following items on the back of the business card.

Combination Diet
Chicken Diet
Beef Diet
Lamb Diet
 

Thanks,

Tobias

All, I will also want a QR code on the front or back of the card that can be scanned by a smart phone with our individual contact information.  Thanks, Tobias

Industry/Entity Type

Pet

```html
<!DOCTYPE html>
<html lang="en">
<head>
<meta charset="utf-8">
<title>Meadowtail Pet Business Card</title>
<link rel="stylesheet" href="https://fonts.googleapis.com/css2?family=Open+Sans:wght@400;600;700;800&display=swap">
<style>
  :root {
    --canvas: #ffffff;
    --card: #2b1710;
    --label: #e2622c;
    --value: #d9804a;
    --title: #e48a2c;
    --name: #ffffff;
    --caption: #333333;
    --brand: #f08a1e;
    --tagline: #f2f0ea;
    --combination: #c9452c;
    --chicken: #e2622a;
    --beef: #f08a1e;
    --lamb: #f4c41a;
  }
  * { box-sizing: border-box; margin: 0; padding: 0; }
  html, body {
    width: 1200px; height: 1024px; overflow: hidden;
    background: var(--canvas);
    font-family: "Open Sans", Arial, sans-serif;
  }
  .sheet { position: relative; width: 1200px; height: 1024px; }
  .card {
    position: absolute; left: 300px; width: 601px; height: 364px;
    background: var(--card);
  }
  .card--front { top: 100px; }
  .card--back { top: 524px; }
  .side-caption {
    position: absolute; left: 0; width: 1200px; text-align: center;
    font-size: 19px; color: var(--caption); letter-spacing: 0.5px;
  }
  .side-caption--front { top: 480px; }
  .side-caption--back { top: 906px; }

  .brand-name {
    position: absolute; left: 0; width: 601px; top: 58px; text-align: center;
    font-size: 36px; font-weight: 700; color: var(--brand); line-height: 1;
  }
  .brand-tagline {
    position: absolute; left: 0; width: 601px; top: 112px; text-align: center;
    font-size: 11px; font-weight: 700; color: var(--tagline); letter-spacing: 1px;
  }
  .person-name {
    position: absolute; left: 0; width: 601px; top: 172px; text-align: center;
    font-size: 19px; color: var(--name); letter-spacing: 0.5px;
  }
  .person-title {
    position: absolute; left: 0; width: 601px; top: 198px; text-align: center;
    font-size: 19px; color: var(--title);
  }
  .contact { position: absolute; font-size: 15px; color: var(--value); white-space: nowrap; }
  .contact b { color: var(--label); font-weight: 700; }
  .contact--email { left: 23px; top: 242px; }
  .contact--web { left: 23px; top: 277px; }
  .contact--sales { left: 23px; top: 312px; }
  .contact--tollfree { left: 356px; top: 242px; }
  .contact--direct { left: 356px; top: 270px; }

  .diet-list { list-style: none; }
  .diet {
    position: absolute; left: 0; width: 601px; text-align: center;
    font-size: 34px; line-height: 1;
  }
  .diet strong { font-weight: 800; }
  .diet span { font-weight: 400; }
  .diet--combination { top: 57px; color: var(--combination); }
  .diet--chicken { top: 130px; color: var(--chicken); }
  .diet--beef { top: 202px; color: var(--beef); }
  .diet--lamb { top: 274px; color: var(--lamb); }
</style>
</head>
<body>
<main class="sheet">
  <section class="card card--front">
    <div class="brand-name">meadowtailpet</div>
    <div class="brand-tagline">100% NATURAL RAW DOG FOOD</div>
    <div class="person-name">RAVI WELBY</div>
    <div class="person-title">Customer experience officer</div>
    <div class="contact contact--email"><b>EMAIL:</b>rwelby@meadowtailpet-example.net</div>
    <div class="contact contact--web"><b>WEBSITE:</b>www.meadowtailpet-example.net</div>
    <div class="contact contact--sales"><b>SALES INQUIRIES:</b>(800)xxx-xxxx</div>
    <div class="contact contact--tollfree"><b>TOLL FREE:</b>xxx-xxx-xxxx</div>
    <div class="contact contact--direct"><b>DIRECT:</b>(347)xxx-xxxx</div>
  </section>
  <p class="side-caption side-caption--front">FRONT</p>

  <section class="card card--back">
    <ul class="diet-list">
      <li class="diet diet--combination"><strong>COMBINATION</strong>&nbsp; <span>DIET</span></li>
      <li class="diet diet--chicken"><strong>CHICKEN</strong> <span>DIET</span></li>
      <li class="diet diet--beef"><strong>BEEF</strong> <span>DIET</span></li>
      <li class="diet diet--lamb"><strong>LAMB</strong> <span>DIET</span></li>
    </ul>
  </section>
  <p class="side-caption side-caption--back">BACK</p>
</main>
</body>
</html>
```